Business Card for Yachting Management Company

Need a business card design for a new yachting project management company. Attached is the logo for the company.
Our clients are large yacht owners and captains.
Design must be in the style of the logo. Modern, elegant.

Example of data to show:
Peter Hollis
Project Manager
(+34) 612 738 104
peter@quorvane.net
Quorvane Management - Meridel Tower, Office 22 - KRB - Palma de Mallorca

The data above will have to be changed (by me) for the different people in the company over the next years.

Will be printed using PrintNova (Lustre Card Series). They provide these guidelines for the size:
"the actual size of the card is 1050 x 600 pixels. However, the full bleed size is 1083 x 633 pixels, and the safe printing area is 1008 x 558 pixels."

```html
<!DOCTYPE html>
<html lang="en">
<head>
<meta charset="utf-8">
<title>Quorvane Management – Business Card</title>
<link rel="stylesheet" href="https://fonts.googleapis.com/css2?family=Montserrat:wght@400;500;600&display=swap">
<style>
  :root {
    --stage: #3a3a3c;
    --card-black: #161616;
    --card-white: #ffffff;
    --brand-blue: #0a6ebd;
    --text-light: #f2f2f2;
  }
  html, body {
    margin: 0;
    width: 1200px;
    height: 1200px;
    overflow: hidden;
    background: var(--stage);
    font-family: "Montserrat", sans-serif;
  }
  .stage {
    width: 1200px;
    height: 1200px;
    display: flex;
    flex-direction: column;
    align-items: center;
    justify-content: center;
    gap: 60px;
  }
  .card {
    position: relative;
    width: 900px;
    height: 514px;
    border-radius: 34px;
    overflow: hidden;
    background: var(--card-black);
    box-shadow: 0 16px 40px rgba(0,0,0,.45);
  }
  .card-shape {
    position: absolute;
    inset: 0;
    width: 100%;
    height: 100%;
  }
  .contact-block {
    position: absolute;
    left: 64px;
    top: 176px;
    color: var(--text-light);
  }
  .identity {
    border-left: 7px solid var(--brand-blue);
    padding-left: 16px;
    margin-bottom: 34px;
  }
  .person-name {
    margin: 0;
    color: var(--brand-blue);
    font-size: 40px;
    font-weight: 600;
    letter-spacing: .5px;
    line-height: 1.05;
    text-transform: uppercase;
  }
  .person-role {
    margin: 2px 0 0;
    font-size: 24px;
    font-weight: 500;
  }
  .details {
    list-style: none;
    margin: 0;
    padding: 0;
    font-size: 20px;
    font-weight: 500;
    line-height: 1.25;
  }
  .details li {
    display: flex;
    align-items: flex-start;
    gap: 14px;
    margin-bottom: 8px;
  }
  .detail-icon {
    flex: none;
    width: 24px;
    height: 24px;
    margin-top: 1px;
  }
  .wordmark-front {
    position: absolute;
    left: 590px;
    top: 165px;
    width: 260px;
    text-align: center;
    color: var(--brand-blue);
    font-size: 28px;
    font-weight: 600;
    letter-spacing: 3px;
    line-height: 1.3;
    text-transform: uppercase;
    white-space: nowrap;
  }
  .card-back {
    display: flex;
    align-items: center;
    justify-content: center;
    background: linear-gradient(100deg, #111 0%, #1b1b1b 45%, #141414 100%);
  }
  .wordmark-back {
    color: var(--brand-blue);
    font-size: 72px;
    font-weight: 600;
    letter-spacing: 8px;
    line-height: 1.2;
    text-align: center;
    text-transform: uppercase;
  }
</style>
</head>
<body>
<main class="stage">

  <section class="card card-front" aria-label="Business card front">
    <svg class="card-shape" viewBox="0 0 900 514" preserveAspectRatio="none" aria-hidden="true">
      <polygon points="300,0 900,0 900,514 590,514 505,232" fill="var(--card-white)"/>
      <polyline points="318,0 520,226 606,514" fill="none" stroke="var(--brand-blue)" stroke-width="6"/>
    </svg>

    <div class="contact-block">
      <div class="identity">
        <h1 class="person-name">Peter Hollis</h1>
        <p class="person-role">Project Manager</p>
      </div>
      <ul class="details">
        <li>
          <svg class="detail-icon" viewBox="0 0 24 24" aria-hidden="true"><path fill="var(--brand-blue)" d="M6.6 10.8a15.1 15.1 0 0 0 6.6 6.6l2.2-2.2c.3-.3.7-.4 1-.2 1.1.4 2.3.6 3.6.6.6 0 1 .4 1 1V20c0 .6-.4 1-1 1A17 17 0 0 1 3 4c0-.6.4-1 1-1h3.5c.6 0 1 .4 1 1 0 1.3.2 2.5.6 3.6.1.3 0 .7-.2 1z"/></svg>
          <span>(+34) 612 738 104</span>
        </li>
        <li>
          <svg class="detail-icon" viewBox="0 0 24 24" aria-hidden="true"><rect x="2" y="5" width="20" height="14" rx="1.5" fill="var(--brand-blue)"/><path d="M2.5 6l9.5 7 9.5-7" fill="none" stroke="var(--card-black)" stroke-width="1.6"/></svg>
          <span>peter@quorvane.net</span>
        </li>
        <li>
          <svg class="detail-icon" viewBox="0 0 24 24" aria-hidden="true"><path fill="var(--brand-blue)" d="M12 2a7 7 0 0 0-7 7c0 5.2 7 13 7 13s7-7.8 7-13a7 7 0 0 0-7-7zm0 9.5A2.5 2.5 0 1 1 12 6.5a2.5 2.5 0 0 1 0 5z"/></svg>
          <span>Quorvane Management - Meridel Tower<br>Office 22 - KRB - Palma de Mallorca</span>
        </li>
      </ul>
    </div>

    <div class="wordmark-front">Quorvane<br>Management</div>
  </section>

  <section class="card card-back" aria-label="Business card back">
    <div class="wordmark-back">Quorvane<br>Management</div>
  </section>

</main>
</body>
</html>
```